Marisol transparent business card

I would like to have a transparent business card created.
A simple yet classy card with
Website www.MarisolPennywhite.com
Phone # 555-417-2936
I would like my full photo on the card as well as my logo.

Target Market(s)

The business card will be printed on transparent card stock.
Www.MarisolPennywhite.com
Phone 555-417-2936
I would like my pic on the card and my logo
Author, Speaker, & Wealth architect

Industry/Entity Type

Business

Contact Information for Business Card

Www.MarisolPennywhite.com
Phone 555-417-2936

Font styles to use
Serif
Decorative
Script

Requirements
Must have
• The business card will be printed on transparent card stock.
• Www.MarisolPennywhite.com
• Phone 555-417-2936
• I would like my pic on the card and my logo
• Author, Speaker, & Wealth architect
Nice to have
• If I could have the tattoo on my pic blurred out or airbrushed over

```html
<!DOCTYPE html>
<html lang="en">
<head>
<meta charset="utf-8">
<title>Marisol Pennywhite – Business Card</title>
<link rel="stylesheet" href="https://fonts.googleapis.com/css2?family=Cinzel:wght@500;700&family=Great+Vibes&family=Libre+Baskerville&display=swap">
<style>
  :root {
    --page-bg: #d6d0c8;
    --frost-light: #f3f4f5;
    --frost-mid: #e1e4e7;
    --gold-light: #e9c488;
    --gold: #b8833a;
    --gold-deep: #7d4f1c;
    --ink: #2b2521;
    --contact-ink: #3a3430;
  }
  * { margin: 0; padding: 0; box-sizing: border-box; }
  html, body {
    width: 1200px; height: 969px; overflow: hidden;
    background: var(--page-bg);
  }
  .canvas { position: relative; width: 1200px; height: 969px; }
  .card {
    position: absolute; left: 60px; top: 178px;
    width: 1080px; height: 612px;
    border-radius: 26px; overflow: hidden;
    background: linear-gradient(160deg, var(--frost-light) 0%, var(--frost-mid) 100%);
    box-shadow: 0 10px 30px rgba(0,0,0,0.18);
  }
  .card-art { position: absolute; inset: 0; }
  .portrait {
    position: absolute; left: 39px; top: 14px;
    width: 236px; height: 294px;
    background: linear-gradient(180deg, #6b4a3a 0%, #3b2a24 45%, #1e1a19 100%);
    border-radius: 4px 4px 0 0;
  }
  .role {
    position: absolute; left: 46px; top: 322px;
    font-family: "Cinzel", serif; font-weight: 500;
    font-size: 31px; line-height: 45px;
    color: var(--gold);
  }
  .contacts {
    position: absolute; left: 52px; top: 418px;
    list-style: none;
  }
  .contacts li {
    display: flex; align-items: center;
    height: 43.5px;
    font-family: "Libre Baskerville", serif;
    font-size: 23px; color: var(--contact-ink);
  }
  .contacts .icon { width: 24px; height: 24px; margin-right: 18px; flex: none; }
  .contacts .square { width: 20px; height: 20px; margin: 0 20px 0 2px; background: var(--gold); flex: none; }
  .brand-mark {
    position: absolute; left: 676px; top: 148px;
    width: 140px; height: 140px; border-radius: 50%;
    border: 4px solid var(--gold);
    display: flex; align-items: center; justify-content: center;
    font-family: "Cinzel", serif; font-weight: 700;
    font-size: 16px; color: var(--gold);
  }
  .brand-name {
    position: absolute; left: 480px; top: 298px; width: 540px;
    text-align: center;
    font-family: "Great Vibes", cursive; font-weight: 400;
    font-size: 60px; line-height: 70px;
    color: var(--gold);
    white-space: nowrap;
  }
  .tagline {
    position: absolute; left: 480px; top: 372px; width: 540px;
    text-align: center;
    font-family: "Cinzel", serif; font-weight: 700;
    font-size: 17px; letter-spacing: 0.5px;
    color: var(--ink);
    white-space: nowrap;
  }
</style>
</head>
<body>
<main class="canvas">
  <section class="card">
    <svg class="card-art" width="1080" height="612" viewBox="0 0 1080 612" aria-hidden="true">
      <defs>
        <linearGradient id="goldSweep" x1="0" y1="0" x2="1" y2="0">
          <stop offset="0.55" stop-color="#b8833a" stop-opacity="0"/>
          <stop offset="0.8" stop-color="#c99550" stop-opacity="0.8"/>
          <stop offset="1" stop-color="#8a5a22"/>
        </linearGradient>
        <linearGradient id="goldRing" x1="0" y1="0" x2="1" y2="1">
          <stop offset="0" stop-color="#e9c488"/>
          <stop offset="0.5" stop-color="#a8712c"/>
          <stop offset="1" stop-color="#7d4f1c"/>
        </linearGradient>
        <mask id="outsideRing">
          <rect width="1080" height="612" fill="#fff"/>
          <circle cx="756" cy="300" r="308" fill="#000"/>
        </mask>
      </defs>
      <rect class="gold-wash" width="1080" height="612" fill="url(#goldSweep)" mask="url(#outsideRing)"/>
      <circle class="gold-ring" cx="756" cy="300" r="308" fill="none" stroke="url(#goldRing)" stroke-width="7"/>
    </svg>

    <div class="portrait" role="img" aria-label="Portrait photo of Marisol Pennywhite, arms crossed, in a black dress"></div>

    <h2 class="role">Author, Speaker<br>&amp; Wealth architect</h2>

    <ul class="contacts">
      <li>
        <svg class="icon" viewBox="0 0 24 24" aria-hidden="true"><path fill="#b8833a" d="M6.6 10.8a15.1 15.1 0 0 0 6.6 6.6l2.2-2.2a1 1 0 0 1 1-.25 11.4 11.4 0 0 0 3.6.57 1 1 0 0 1 1 1V20a1 1 0 0 1-1 1A17 17 0 0 1 3 4a1 1 0 0 1 1-1h3.5a1 1 0 0 1 1 1c0 1.25.2 2.45.57 3.57a1 1 0 0 1-.25 1z"/></svg>
        555-417-2936
      </li>
      <li>
        <svg class="icon" viewBox="0 0 24 24" aria-hidden="true"><rect x="2" y="5" width="20" height="14" rx="1.5" fill="#b8833a"/><path d="M2.5 6 12 13l9.5-7" fill="none" stroke="#f0ede8" stroke-width="1.6"/></svg>
        Info@MarisolPennywhite.com
      </li>
      <li>
        <svg class="icon" viewBox="0 0 24 24" aria-hidden="true"><circle cx="12" cy="12" r="9.5" fill="none" stroke="#b8833a" stroke-width="2"/><ellipse cx="12" cy="12" rx="4" ry="9.5" fill="none" stroke="#b8833a" stroke-width="1.6"/><path d="M2.5 12h19M4 7h16M4 17h16" stroke="#b8833a" stroke-width="1.4"/></svg>
        www.MarisolPennywhite.com
      </li>
      <li>
        <span class="square" aria-hidden="true"></span>
        MarisolPennywhite.com
      </li>
    </ul>

    <div class="brand-mark">Pennywhite</div>
    <h1 class="brand-name">Marisol Pennywhite</h1>
    <p class="tagline">LIVE WITH INTENTION. BUILD REAL WEALTH</p>
  </section>
</main>
</body>
</html>
```